Public Relations Agency Seeks Wordpress Design and Coding

TORVEX Media is a public relations agency specializing in media relations, public affairs and marketing communication.

The site should display the following visual characteristics: professionalism, trustworthiness, high-tech focus, clear and concise design.

The desired colors are royal blue, gray and hints of red.

Design look/feel inspired by this site: http://brisklanefetes.example/

Specifications:

1. Navigation/Pages/Index:

HOME

ABOUT US

SERVICES

NEWS

CONTACT

---

2. Functionality of/content for each page:

- Home
o Dominant photo (professional, edgy, innovative)
o Simple, straightforward access to/from “Home” from other pages
o Includes logo (attached) and tagline "Unleash the power of communication"
o Direct link to “CONTACT”
o Links to social media accounts: Facebook, Twitter, LinkedIn

- About Us

o Company profile blurb
o President’s photo with short bio

- Services
o Public Relations
 Strategic communication
 Brand and reputation management
 Community relations
o Media Relations
 News coverage and contacts
 Media training and interview skills
 Crisis communications
o Congressional Affairs
 Public affairs
 Public policy
 Legislative strategy
o Mass Communication
 Speechwriting
 Presentation creation
 Social media
o Marketing Communications
 Business collateral material
 Promotional campaigns
 Special events and tradeshows

- News
o Blog-like page to post information and/or share news from other sites

- Contact
o Standard “Contact Us” form (Name, Email, Phone, Message)
o Direct Contact
 (555) 314-2690
 Marlow@TORVEXmedia.example

Target Market(s)

Small to large businesses specializing in high technology, defense/military, medicine/healthcare, and wide array of professional services.

Industry/Entity Type

Marketing

Font styles to use
Serif
Sans Serif

Colors
0555a3
ec2027
edf3f7

Requirements
Must have
• -- Project reqires DESIGN - and - fully CODED.

-- Strong SEO

-- Optimized for mobile viewing

Thank you!

```html
<!DOCTYPE html>
<html lang="en">
<head>
<meta charset="utf-8">
<title>TORVEX Media – Public Relations</title>
<link href="https://fonts.googleapis.com/css2?family=Open+Sans:wght@400;600;700&display=swap" rel="stylesheet">
<style>
:root{
  --royal:#0555a3;
  --red:#ec2027;
  --mist:#edf3f7;
  --ink:#333;
  --muted:#777;
  --footer:#2b2b2b;
  --footer-deep:#1e1e1e;
  --white:#fff;
}
*{box-sizing:border-box;margin:0;padding:0}
html,body{width:688px;height:1200px;overflow:hidden;background:#fff}
body{font-family:"Open Sans",Arial,sans-serif;color:var(--ink);position:relative}
.abs{position:absolute}

/* header */
.site-header{position:absolute;left:0;top:0;width:688px;height:75px;background:#fff}
.brand{left:76px;top:22px;font-size:24px;font-weight:700;color:#3a3a3a;letter-spacing:1px}
.brand small{display:block;font-size:10px;font-weight:600;letter-spacing:4px;text-align:center;color:#3a3a3a;margin-top:-4px}
.call{right:40px;top:10px;font-size:11px;color:var(--muted)}
.call b{color:var(--red);font-weight:600}
.nav{right:40px;top:40px;display:flex;gap:6px}
.nav a{font-size:10px;color:#555;text-decoration:none;padding:5px 10px;border:1px solid transparent}
.nav a.active{border-color:var(--red);color:var(--red)}

/* hero */
.hero{left:0;top:75px;width:688px;height:257px;background:linear-gradient(90deg,#c6ccd4 0%,#dfe3e8 45%,#f0ede9 75%,#e6e0da 100%)}
.hero-people{left:0;top:0;width:360px;height:257px;background:linear-gradient(180deg,#d9dde2 0%,#b8a89a 60%,#8e7c6e 100%);opacity:.6}
.hero-lead{left:420px;top:0;width:230px;height:257px;background:radial-gradient(ellipse at 50% 45%,#c9a38a 0%,#b98f76 35%,#e9e4df 75%)}
.tagline{left:76px;font-size:22px;font-weight:700;color:#fff;background:rgba(5,40,90,.78);padding:4px 10px;line-height:1.3}
.slide-ctrl{top:292px;width:20px;height:18px;background:rgba(40,40,40,.7);display:flex;align-items:center;justify-content:center}

/* about */
.section-title{width:688px;text-align:center;font-size:20px;font-weight:600;color:var(--royal)}
.section-title .rule{display:block;width:40px;height:2px;background:var(--red);margin:6px auto 0}
.portrait{left:80px;top:402px;width:73px;height:84px;background:linear-gradient(180deg,#cfd6de 0%,#d9b9a3 55%,#c43a3a 100%)}
.about-copy{left:174px;top:403px;width:430px;font-size:9px;line-height:1.55;color:var(--muted)}
.btn-outline{left:174px;top:458px;font-size:9px;color:var(--red);border:1px solid var(--red);padding:4px 10px}

/* services */
.services{left:0;top:508px;width:688px;height:292px;background:var(--mist)}
.services-sub{width:688px;top:560px;text-align:center;font-size:10px;color:var(--red)}
.card{top:590px;width:166px;height:188px;background:#fff}
.card .photo{height:104px}
.card h3{font-size:11px;font-weight:600;text-align:center;color:#333;margin-top:10px}
.card p{font-size:8px;line-height:1.5;text-align:center;color:var(--muted);padding:4px 14px 0}
.card .more{display:block;text-align:center;font-size:8px;color:var(--red);margin-top:3px}

/* news */
.news-item{top:874px;width:180px}
.date{position:absolute;left:0;top:0;width:38px;height:40px;text-align:center;border:1px solid #ddd;color:#aaa}
.date b{display:block;font-size:17px;font-weight:400;line-height:24px}
.date span{display:block;font-size:8px;background:#eee;line-height:14px}
.date.current{background:var(--red);border-color:var(--red);color:#fff}
.date.current span{background:#c2141a;color:#fff}
.news-text{position:absolute;left:46px;top:0;width:130px;font-size:8px;line-height:1.5;color:var(--muted)}
.news-text em{font-style:normal;color:var(--red);display:block;margin-top:2px}

/* footer */
.site-footer{left:0;top:962px;width:688px;height:218px;background:var(--footer)}
.footer-title{top:986px;width:688px;text-align:center;font-size:16px;color:#fff}
.footer-title .accent{color:#7fb2e5}
.footer-sub{top:1008px;width:688px;text-align:center;font-size:8px;color:#999}
.field{background:#fff;border:1px solid #ccc;font-size:8px;color:#999;padding:5px 6px;height:20px}
.submit{left:265px;top:1126px;font-size:9px;color:#fff;background:#444;border:1px solid #555;padding:4px 12px}
.contact-line{left:400px;font-size:9px;color:#ccc;display:flex;align-items:center;gap:8px}
.contact-line svg{flex:none}
.social{top:1124px;left:400px;display:flex;gap:6px}
.social span{width:14px;height:14px;border-radius:50%;background:#bbb}
.copyright{left:0;top:1180px;width:688px;height:20px;background:var(--footer-deep);text-align:center;font-size:7px;line-height:20px;color:#888}
</style>
</head>
<body>

<header class="site-header">
  <div class="abs brand">TORVEX<small>MEDIA</small></div>
  <div class="abs call">Call Us: <b>1800 555 019</b></div>
  <nav class="abs nav">
    <a class="active">Home</a><a>About Us</a><a>Services</a><a>News</a><a>Contact us</a>
  </nav>
</header>

<section class="abs hero">
  <div class="abs hero-people" role="img" aria-label="Team of colleagues collaborating at a table"></div>
  <div class="abs hero-lead" role="img" aria-label="Smiling professional woman"></div>
</section>
<div class="abs tagline" style="top:158px">Unleash The Power of</div>
<div class="abs tagline" style="top:192px">Communication</div>
<div class="abs slide-ctrl" style="left:76px"><svg width="8" height="8" viewBox="0 0 8 8"><path d="M5 1 2 4l3 3" stroke="#fff" fill="none" stroke-width="1.4"/></svg></div>
<div class="abs slide-ctrl" style="left:98px"><svg width="8" height="8" viewBox="0 0 8 8"><path d="M3 1l3 3-3 3" stroke="#fff" fill="none" stroke-width="1.4"/></svg></div>

<section>
  <h2 class="abs section-title" style="top:366px">About Us<span class="rule"></span></h2>
  <div class="abs portrait" role="img" aria-label="Portrait of the agency president"></div>
  <p class="abs about-copy">Lorem ipsum dolor sit amet, consectetur adipisicing elit, sed do eiusmod tempor incididunt ut labore et dolore magna aliqua. Ut enim ad minim veniam, quis nostrud exercitation ullamco laboris nisi ut aliquip ex ea commodo consequat. Duis aute irure dolor in reprehenderit in voluptate velit esse cillum dolore eu fugiat.</p>
  <a class="abs btn-outline">Learn More</a>
</section>

<section class="abs services"></section>
<h2 class="abs section-title" style="top:532px">Servcies</h2>
<p class="abs services-sub">We are public relations agency specializing in</p>

<article class="abs card" style="left:76px">
  <div class="photo" role="img" aria-label="Paper figures holding hands" style="background:linear-gradient(180deg,#9a9a9a,#d6d6d6)"></div>
  <h3>Media Relations</h3>
  <p>Lorem ipsum dolor sit amet, consectetur adipiscing elit, sed do et ut aliqua.</p>
  <span class="more">Read More &gt;&gt;</span>
</article>
<article class="abs card" style="left:261px">
  <div class="photo" role="img" aria-label="Business people shaking hands before a government building" style="background:linear-gradient(180deg,#c5cfd9,#6d7580)"></div>
  <h3>Public Affairs</h3>
  <p>Lorem ipsum dolor sit amet, consectetur adipiscing elit, sed do et ut aliqua.</p>
  <span class="more">Read More &gt;&gt;</span>
</article>
<article class="abs card" style="left:447px">
  <div class="photo" role="img" aria-label="Professional working at a computer" style="background:linear-gradient(180deg,#e6edf3,#8aa4bf)"></div>
  <h3>Marketing Communication</h3>
  <p>Lorem ipsum dolor sit amet, consectetur adipiscing elit, sed do et ut aliqua.</p>
  <span class="more">Read More &gt;&gt;</span>
</article>

<h2 class="abs section-title" style="top:830px">Latest News</h2>
<article class="abs news-item" style="left:80px">
  <div class="date current"><b>05</b><span>Sept</span></div>
  <p class="news-text">Lorem ipsum dolor sit amet, sit consectetur adipisicing elit, sed do eiusmod tempor.<em>Read More &gt;&gt;</em></p>
</article>
<article class="abs news-item" style="left:270px">
  <div class="date"><b>03</b><span>Sept</span></div>
  <p class="news-text">Lorem ipsum dolor sit amet, sit consectetur adipisicing elit, sed do eiusmod tempor.<em>Read More &gt;&gt;</em></p>
</article>
<article class="abs news-item" style="left:456px">
  <div class="date"><b>01</b><span>Sept</span></div>
  <p class="news-text">Lorem ipsum dolor sit amet, sit consectetur adipisicing elit, sed do eiusmod tempor.<em>Read More &gt;&gt;</em></p>
</article>

<footer>
  <div class="abs site-footer"></div>
  <h2 class="abs footer-title">Contact <span class="accent">Us</span></h2>
  <p class="abs footer-sub">Let's talk business, get in touch!</p>
  <div class="abs field" style="left:80px;top:1044px;width:118px">Enter Name</div>
  <div class="abs field" style="left:206px;top:1044px;width:118px">Enter Email</div>
  <div class="abs field" style="left:80px;top:1074px;width:118px">Enter Phone</div>
  <div class="abs field" style="left:206px;top:1074px;width:118px;height:42px">Enter Message</div>
  <div class="abs submit">Submit</div>

  <div class="abs contact-line" style="top:1046px">
    <svg width="10" height="12" viewBox="0 0 10 12"><path d="M5 11S1 6.5 1 4a4 4 0 0 1 8 0c0 2.5-4 7-4 7z" fill="#bbb"/><circle cx="5" cy="4" r="1.5" fill="#2b2b2b"/></svg>
    111, Building Name, City, Zipcode
  </div>
  <div class="abs contact-line" style="top:1072px">
    <svg width="10" height="12" viewBox="0 0 10 12"><path d="M2 1h2l1 3-1.5 1a6 6 0 0 0 3 3L8 6.5l2 1v2.5C5 10 1 6 1 2z" fill="#bbb"/></svg>
    Call Us : +61 (0)400 555 127
  </div>
  <div class="abs contact-line" style="top:1098px">
    <svg width="11" height="9" viewBox="0 0 11 9"><rect x=".5" y=".5" width="10" height="8" fill="#bbb"/><path d="M.5.5l5 4 5-4" stroke="#2b2b2b" fill="none"/></svg>
    Email : hello@torvexmedia.example
  </div>
  <div class="abs social"><span></span><span></span><span></span><span></span></div>
  <div class="abs copyright">Copyright 2014 TORVEX Media. All Rights Reserved</div>
</footer>

</body>
</html>
```